complete redesign of prelmorax.com , responsive design

Present website should be used for ideation purpose, designer should submit best design which can explain visitor and excite them to download the app.
. By looking at default view of website, students should get the idea about product.

This website to explain about tablet app and it's features, benefits for students, parents and institutes.

This is tablet/Vexo based product to prepare National ( KMR, ZORWN, PUV, Brennick etc) and International competitive exams (YLD, KUW, QVF, DRUX etc) and visitor should get ideas by just looking at the home page.

Institutes can publish their content on Vornaplex.

Student can optimize time and performance on Vornaplex.

Content is same as present website and please use app screenshot to explain the product. screens should be used wherever relevant, refer attached screens. Website must be responsive and easy in navigation.
This is cloud based system and offering prep test , analysis and dynamic testing as per their study plan.

Education

Education

Coded - Design and coding required

5+ page

6b449b
886aae
b7a5cd
e4daeb
f3f1f8
ffffff

• Great design , responsive, easy to grasp the idea. Allow option to register for free app download.
• Project must have all pages as it is in present website.
• I will leave designer to come up with presentation.
• It should not be layout as it is today. Lot of design being submitted by changing just color and icons. I request to come up with your style and you can use contents from present website.

```html
<!DOCTYPE html>
<html lang="en">
<head>
<meta charset="utf-8">
<title>Prelmorax — Vornaplex</title>
<link href="https://fonts.googleapis.com/css2?family=Open+Sans:wght@300;400;600;700&display=swap" rel="stylesheet">
<style>
:root{
  --purple:#6b449b;
  --purple-mid:#886aae;
  --purple-soft:#b7a5cd;
  --lilac:#e4daeb;
  --mist:#f3f1f8;
  --white:#ffffff;
  --ink:#3b3b47;
  --muted:#8a8a96;
  --line:#e2e2e8;
  --night:#363249;
  --night-deep:#27243a;
}
*{box-sizing:border-box;margin:0;padding:0}
html,body{width:1200px;height:3188px;overflow:hidden}
body{font-family:"Open Sans",Arial,sans-serif;color:var(--ink);background:var(--white);position:relative}
.wrap{position:absolute;left:0;width:1200px}

/* header */
.site-header{top:0;height:100px;background:var(--white);border-bottom:1px solid var(--line)}
.brand{position:absolute;left:110px;top:30px;display:flex;align-items:center;gap:10px}
.brand-dot{width:38px;height:38px;border-radius:50%;background:var(--purple)}
.brand-name{font-size:22px;font-weight:700;color:var(--purple)}
.main-nav{position:absolute;right:110px;top:34px;display:flex;align-items:center;gap:44px;font-size:13px;font-weight:600;text-transform:uppercase;color:var(--ink)}
.main-nav .active{color:var(--purple)}
.btn-signup{background:var(--purple);color:var(--white);padding:9px 20px;border-radius:3px}

/* hero */
.hero{top:100px;height:540px;background:linear-gradient(180deg,#f0eff3,#dedde3)}
.hero-photo{position:absolute;left:600px;top:0;width:480px;height:540px;background:linear-gradient(160deg,#d7cfc4,#c9b79f 45%,#8bb7d8 70%,#e8e4df)}
.hero-copy{position:absolute;left:110px;top:145px;width:470px}
.hero-copy h1{font-size:34px;font-weight:400;line-height:1.3;color:#333}
.hero-copy p{font-size:14px;color:var(--muted);margin-top:14px;line-height:1.6}
.btn-register{display:inline-block;margin-top:26px;background:var(--purple);color:var(--white);font-size:14px;font-weight:600;padding:15px 34px;border-radius:3px;text-transform:uppercase}
.platforms{display:flex;gap:14px;margin-top:22px}
.platforms span{width:22px;height:22px;border-radius:50%;background:var(--purple)}
.slider-dots{position:absolute;left:0;right:0;bottom:20px;display:flex;justify-content:center;gap:8px}
.slider-dots span{width:9px;height:9px;border-radius:50%;background:#c7c5cf}
.slider-dots .on{background:var(--purple)}

/* platform */
.platform{top:640px;height:660px;background:var(--white)}
.section-title{text-align:center;font-size:36px;font-weight:400;color:#333}
.section-title em{font-style:normal;color:var(--purple)}
.section-lead{width:980px;margin:18px auto 0;text-align:center;font-size:13px;line-height:1.8;color:var(--muted)}
.platform .section-title{margin-top:80px}
.tab-label{text-align:center;font-size:20px;font-weight:600;margin-top:42px;color:#333}
.tab-rule{width:1000px;height:1px;background:var(--line);margin:14px auto 0}
.students-photo{position:absolute;left:90px;top:330px;width:230px;height:300px;background:linear-gradient(180deg,#e9e3da,#b3a48e 50%,#4d6d97)}
.feature-grid{position:absolute;left:360px;top:340px;width:740px;display:grid;grid-template-columns:1fr 1fr;gap:40px 60px}
.feature{display:flex;gap:16px}
.feature-icon{flex:none;width:52px;height:52px;border-radius:50%;background:var(--purple);display:flex;align-items:center;justify-content:center}
.feature h3{font-size:17px;font-weight:600;color:#333;margin-top:12px}
.feature p{font-size:12px;line-height:1.7;color:var(--muted);margin-top:8px}
.arrow{position:absolute;top:460px;font-size:22px;color:#555}
.read-more{position:absolute;right:110px;top:600px;font-size:14px;font-weight:600;color:var(--purple)}

/* how to use */
.how{top:1300px;height:380px;background:linear-gradient(180deg,var(--purple-mid),var(--purple))}
.how-crowd{position:absolute;left:0;right:0;bottom:0;height:150px;background:linear-gradient(180deg,rgba(80,48,122,0),rgba(80,48,122,.8))}
.how-copy{position:absolute;left:110px;top:60px;width:560px;color:var(--white)}
.how-copy h2{font-size:30px;font-weight:600}
.how-copy p{font-size:12px;line-height:1.8;margin-top:16px;color:var(--lilac)}
.how-tablet{position:absolute;left:720px;top:40px;width:330px;height:270px;border-radius:16px;background:linear-gradient(160deg,#f6f2ea,#d9c7a5 55%,#b99467)}

/* everything */
.everything{top:1680px;height:820px;background:var(--white)}
.everything .section-title{margin-top:70px}
.audience{position:absolute;top:250px;width:300px;height:480px;border:1px solid var(--line);background:var(--white);text-align:center}
.audience-icon{width:96px;height:96px;border-radius:50%;background:var(--purple);margin:-48px auto 0;display:flex;align-items:center;justify-content:center;border:6px solid var(--white);box-shadow:0 0 0 1px var(--line)}
.audience h3{font-size:20px;font-weight:600;color:#333;margin-top:14px}
.audience ul{list-style:none;text-align:left;margin:20px 26px 0;font-size:12px;line-height:1.55;color:var(--muted)}
.audience li{position:relative;padding:0 0 10px 18px}
.audience li::before{content:"";position:absolute;left:0;top:6px;width:8px;height:8px;background:var(--purple-soft);border-radius:2px}
.btn-know{position:absolute;left:50%;bottom:28px;transform:translateX(-50%);background:var(--purple);color:var(--white);font-size:13px;font-weight:600;padding:12px 30px;border-radius:3px;white-space:nowrap}

/* associates */
.associates{top:2500px;height:260px;background:var(--mist);border-top:1px solid var(--line)}
.associates h2{text-align:center;font-size:28px;font-weight:400;color:#333;margin-top:60px}
.partner-row{display:flex;justify-content:center;align-items:center;gap:40px;margin-top:40px}
.partner{height:56px;background:var(--purple-soft);border-radius:4px}
.partner.round{width:56px;border-radius:50%}

/* subscribe */
.subscribe{top:2760px;height:340px;background:linear-gradient(180deg,var(--night),var(--night-deep));color:var(--white);text-align:center}
.subscribe h2{font-size:26px;font-weight:400;margin-top:60px}
.subscribe p{font-size:12px;color:#b8b4c8;margin-top:12px}
.subscribe-form{display:flex;justify-content:center;margin-top:26px}
.subscribe-form .field{width:340px;height:50px;background:var(--white);color:#aaa;font-size:13px;text-align:left;padding:16px 18px;border-radius:3px 0 0 3px}
.subscribe-form .submit{width:130px;height:50px;background:var(--purple);font-size:14px;font-weight:600;padding-top:15px;border-radius:0 3px 3px 0}
.follow{font-size:20px;margin-top:34px}
.social{display:flex;justify-content:center;gap:18px;margin-top:18px}
.social span{width:38px;height:38px;border-radius:50%;background:var(--purple)}

/* footer */
.site-footer{top:3100px;height:88px;background:#1f1d2c;color:#9b98aa;font-size:12px}
.site-footer .left{position:absolute;left:110px;top:36px}
.site-footer .right{position:absolute;right:110px;top:36px}
</style>
</head>
<body>

<header class="wrap site-header">
  <div class="brand"><span class="brand-dot"></span><span class="brand-name">Prelmorax</span></div>
  <nav class="main-nav">
    <span class="active">Home</span><span>Solution</span><span>Associates</span><span>FAQ</span><span class="btn-signup">Sign Up</span>
  </nav>
</header>

<section class="wrap hero">
  <div class="hero-photo" role="img" aria-label="Smiling student holding books and raising her hand"></div>
  <div class="hero-copy">
    <h1>Exceed your results &amp; enhance your rank with Vornaplex</h1>
    <p>Students score 30% more gain in analysing &amp; checking answers &amp; solutions manually.</p>
    <span class="btn-register">Register Now</span>
    <div class="platforms"><span></span><span></span><span></span></div>
  </div>
  <div class="slider-dots"><span class="on"></span><span></span><span></span></div>
</section>

<section class="wrap platform">
  <h2 class="section-title">The Biggest Platform <em>Ever</em></h2>
  <p class="section-lead">Vornaplex is a cloud based preparation platform for national and international competitive exams. Students practise prep tests, review deep analysis and take dynamic tests planned around their own study schedule, while institutes publish content directly to the tablet app.</p>
  <div class="tab-label">Students</div>
  <div class="tab-rule"></div>
  <div class="students-photo" role="img" aria-label="Two students standing with backpacks and books"></div>
  <span class="arrow" style="left:40px">&#8249;</span>
  <span class="arrow" style="right:40px">&#8250;</span>
  <div class="feature-grid">
    <div class="feature">
      <div class="feature-icon"><svg width="24" height="24" viewBox="0 0 24 24" fill="none" stroke="#fff" stroke-width="2"><rect x="5" y="2" width="14" height="20" rx="2"/><line x1="11" y1="18" x2="13" y2="18"/></svg></div>
      <div><h3>Free App</h3><p>Access the app free of cost for every Vexo tablet user, available on all major stores and ready to start practising straight away.</p></div>
    </div>
    <div class="feature">
      <div class="feature-icon"><svg width="24" height="24" viewBox="0 0 24 24" fill="#fff"><rect x="3" y="13" width="4" height="8"/><rect x="10" y="8" width="4" height="13"/><rect x="17" y="3" width="4" height="18"/></svg></div>
      <div><h3>Analytics</h3><p>Detailed analysis of every test shows strengths, weak topics and time spent so you can improve your rank faster.</p></div>
    </div>
    <div class="feature">
      <div class="feature-icon"><svg width="24" height="24" viewBox="0 0 24 24" fill="none" stroke="#fff" stroke-width="2"><path d="M6 2h9l5 5v15H6z"/><line x1="9" y1="12" x2="17" y2="12"/><line x1="9" y1="16" x2="17" y2="16"/></svg></div>
      <div><h3>Effective Content</h3><p>Questions and solutions written by expert faculty and leading institutes, covering the full syllabus of each exam.</p></div>
    </div>
    <div class="feature">
      <div class="feature-icon"><svg width="24" height="24" viewBox="0 0 24 24" fill="none" stroke="#fff" stroke-width="2"><circle cx="12" cy="12" r="4"/><path d="M12 2v3M12 19v3M2 12h3M19 12h3M5 5l2 2M17 17l2 2M5 19l2-2M17 7l2-2"/></svg></div>
      <div><h3>Custom test</h3><p>Build your own tests by chapter, difficulty and duration to match the study plan you follow each week.</p></div>
    </div>
  </div>
  <span class="read-more">Read More &rsaquo;</span>
</section>

<section class="wrap how">
  <div class="how-crowd" role="img" aria-label="Faint crowd of graduates in silhouette"></div>
  <div class="how-copy">
    <h2>How To Use?</h2>
    <p>Download the free app on your tablet, register with your email and choose the exams you are preparing for. Pick a prep test or create a custom one, attempt it within the set time and submit. Your answers are checked instantly and a full report appears with scores, accuracy and time taken for every question.</p>
    <p>Review detailed solutions, bookmark tough questions and follow the suggested study plan. Dynamic tests adapt to your level so each new test targets the topics where you need the most practice.</p>
  </div>
  <div class="how-tablet" role="img" aria-label="Tablet showing the app test screen"></div>
</section>

<section class="wrap everything">
  <h2 class="section-title">Everything You <em>Need</em></h2>
  <p class="section-lead">One platform connects students, institutes and parents. Students prepare smarter, institutes publish content and track their batches, and parents follow progress with clear reports delivered right to their device.</p>

  <div class="audience" style="left:140px">
    <div class="audience-icon"><svg width="44" height="44" viewBox="0 0 24 24" fill="#fff"><path d="M12 4 1 9l11 5 9-4v6h2V9z"/><path d="M6 13v4c0 2 3 3 6 3s6-1 6-3v-4l-6 3z"/></svg></div>
    <h3>Students</h3>
    <ul>
      <li>Complete platform for the preparation of competitive exams</li>
      <li>Access to real exam pattern tests from leading institutes</li>
      <li>Test level analysis of the test preparation</li>
      <li>Improve time and accuracy with every test</li>
      <li>Track weak topics and revise them easily</li>
      <li>Study anytime with the tablet app</li>
    </ul>
    <span class="btn-know">Know More</span>
  </div>

  <div class="audience" style="left:450px">
    <div class="audience-icon"><svg width="44" height="44" viewBox="0 0 24 24" fill="#fff"><path d="M12 2 2 7h20z"/><rect x="4" y="9" width="2" height="9"/><rect x="9" y="9" width="2" height="9"/><rect x="13" y="9" width="2" height="9"/><rect x="18" y="9" width="2" height="9"/><rect x="2" y="19" width="20" height="3"/></svg></div>
    <h3>Institutes</h3>
    <ul>
      <li>Publish your content on the platform</li>
      <li>Test and batch management tools</li>
      <li>Organize and manage all your content</li>
      <li>Full access to reports of students</li>
      <li>Sell your content to more learners</li>
      <li>Create tests quickly with question banks</li>
      <li>Conduct quick and instant tests for students</li>
    </ul>
    <span class="btn-know">Know More</span>
  </div>

  <div class="audience" style="left:760px">
    <div class="audience-icon"><svg width="44" height="44" viewBox="0 0 24 24" fill="#fff"><circle cx="8" cy="6" r="3"/><circle cx="17" cy="8" r="2.5"/><path d="M2 21v-4c0-3 3-5 6-5s6 2 6 5v4z"/><path d="M14 21v-3c0-2 1.5-4 3-4s5 1 5 4v3z"/></svg></div>
    <h3>Parents</h3>
    <ul>
      <li>Monitor every test in one simple place</li>
      <li>Access child's performance data anytime</li>
      <li>Track the current state of preparation</li>
      <li>Get detailed insight of performance</li>
      <li>Get messages from institutes directly</li>
      <li>Analyse test and time packages in detail</li>
    </ul>
    <span class="btn-know">Know More</span>
  </div>
</section>

<section class="wrap associates">
  <h2>Associates</h2>
  <div class="partner-row">
    <span class="partner round" role="img" aria-label="Partner badge"></span>
    <span class="partner" style="width:110px" role="img" aria-label="Partner badge"></span>
    <span class="partner round" role="img" aria-label="Partner badge"></span>
    <span class="partner" style="width:150px" role="img" aria-label="Partner badge"></span>
    <span class="partner" style="width:130px" role="img" aria-label="Partner badge"></span>
    <span class="partner" style="width:150px" role="img" aria-label="Partner badge"></span>
  </div>
</section>

<section class="wrap subscribe">
  <h2>Subscribe Latest News &amp; Updates</h2>
  <p>Stay informed about new tests, exam dates and feature releases delivered straight to your inbox every month.</p>
  <div class="subscribe-form"><span class="field">Email Address</span><span class="submit">Submit</span></div>
  <div class="follow">Follow On</div>
  <div class="social"><span></span><span></span><span></span><span></span></div>
</section>

<footer class="wrap site-footer">
  <span class="left">About &nbsp;|&nbsp; Privacy Policy</span>
  <span class="right">Copyright &copy; 2014 Prelmorax Inc. All rights reserved.</span>
</footer>

</body>
</html>
```